Larkfold Inn Weekly Special Flyer

Looking for a professional weekly special promotion flyer to handout. Something I can edit and use as specials change. We are a small bar in a rural town (country). Something that can be use everyday software

Larkfold Inn
418 West Cedar Avenue
Wellington, Ohio 44987
(440) 555-0193
Join Us on Gathergram \Larkfoldinn

$1.00 Domestic Drafts every day during happy hour
Happy hour hours = Mon-Fri 3-7 Sat & Sun 12-7

Sundays:
Free Pool ALL day on both tables
$1.00 Domestic drafts until midnight

$3.00 Appetizers
$4.00 Glacine Bloody Marys
$5.00 3 - topping pizza

Mondays:
$2.00 Well Margaritas
$3.00 5 Pebble Vodka Bombs
$4.00 Rum Runners
$6.00 Philly Cheese Steak Sandwich served with loaded fries

Tuesdays:
$2.00 Harvest Radler
$3.00 Gray Heron
$3.00 Loaded Nachos
$3.00 Loaded Fries
$4.00 Liquid Marijuana's

Wednesdays:
$2.00 Quiet Meadow Bottles
$3.00 Blue Stars
$3.00 Fizzle Twigs
$4.00 Bartender Bombs
$4.00 2 Topping Pizzas

Thursdays:
~*~*Ladies Night Thursday*~
$3.00 Tart Crumb
$3.00 Sweet Affair
$3 1/2 dozen wings!
$4.00 Spin Doctors
LADIES ONLY SPECIALS
$2.00 5 Pebble Shots
$3.00 Long Islands
$4.00 Bartender Bombs!

Fridays:
$2.00 Mele Nalu Pineapple Beer
$2.00 Lumbermans brew
$2.00 Knotted Cup
$2.00 Restless Rover
$3.00 Little Beers
$3.00 banana pepper rings...
$3.00 hot pepper cheese balls
$4.00 Washington Apples

Saturdays:
Extended Happy Hour (12-8)
$1.00 Domestic Drafts
$2.00 Wine Coolers
$2.00 Lumbermans Brew
$2.00 Pellows Hard Iced Tea
$3.00 Sweet Affair
$3.00 Irish Breakfast Shots
$4.00 Irish Car Bombs
$4.00 Orbit Lollies
~*Until 8PM*~

add some tear off coupons that I can edit dollars and offers:
$2.00 off Pizza
$2.00 Philly Cheese Steak
Contact for us for birthday party discounts and fund raising events

attached is our company logo

I also attached a flyer of something I liked I picked up

```html
<!DOCTYPE html>
<html lang="en">
<head>
<meta charset="utf-8">
<title>Larkfold Inn – Happy Hours</title>
<link rel="stylesheet" href="https://fonts.googleapis.com/css2?family=Lobster&family=Roboto+Condensed:wght@400;700&family=Arvo:wght@700&family=Roboto:wght@700;900&display=swap">
<style>
:root{
  --wood-dark:#3a1a0c;
  --wood-mid:#6a2f14;
  --wood-light:#8a4220;
  --photo-dark:#1c0d06;
  --photo-amber:#a0581c;
  --orange:#f36f21;
  --orange-deep:#e0521a;
  --green:#8dc63f;
  --red:#e31e24;
  --white:#ffffff;
  --cream:#f3e6d8;
}
*{box-sizing:border-box;margin:0;padding:0}
html,body{width:934px;height:1200px;overflow:hidden}
body{position:relative;background:var(--wood-mid);font-family:"Roboto Condensed",Arial,sans-serif;color:var(--white)}
.abs{position:absolute}

.hero-photo{left:0;top:0;width:934px;height:420px;
  background:radial-gradient(ellipse at 70% 35%,var(--photo-amber) 0%,#5e2c10 40%,var(--photo-dark) 80%)}
.wood{left:0;top:380px;width:934px;height:720px;
  background:linear-gradient(90deg,var(--wood-dark) 0%,var(--wood-light) 30%,var(--wood-mid) 55%,var(--wood-light) 75%,var(--wood-dark) 100%)}
.hero-curve{left:0;top:360px}

.brand{left:70px;top:88px;display:flex;align-items:center;gap:12px}
.brand-dot{width:22px;height:22px;border-radius:50%;background:var(--orange)}
.brand-name{font-family:"Arvo",serif;font-weight:700;font-size:34px;color:var(--white)}

.title{left:68px;top:212px;font-family:"Lobster",cursive;font-size:84px;line-height:1;color:var(--white)}
.hours{left:116px;top:318px;font-family:"Roboto Condensed",sans-serif;font-weight:700;font-size:29px;line-height:36px;text-align:center;color:var(--white)}

.big-price{left:625px;top:245px;width:216px;height:216px;border-radius:50%;background:var(--white);
  display:flex;align-items:center;justify-content:center}
.big-price span{width:196px;height:196px;border-radius:50%;background:radial-gradient(circle at 40% 35%,#ff8a3a,var(--orange-deep));
  display:flex;align-items:center;justify-content:center;font-family:"Roboto",sans-serif;font-weight:900;font-size:110px;color:var(--white)}

.price-badge{width:66px;height:66px;border-radius:50%;background:var(--orange-deep);border:4px solid var(--white);
  display:flex;align-items:center;justify-content:center;font-family:"Roboto",sans-serif;font-weight:900;font-size:30px;color:var(--white)}

.photo{border-radius:50%}
.photo-mug{left:48px;top:555px;width:190px;height:200px;border-radius:18px;background:linear-gradient(160deg,#f4c44a,#c8781a 60%,#222 90%)}
.photo-philly{left:285px;top:485px;width:160px;height:75px;background:radial-gradient(ellipse,#c88a4c,#7a4422 70%,#e9e2d8 72%)}
.photo-nachos{left:510px;top:495px;width:150px;height:80px;background:radial-gradient(ellipse,#e7e2c9,#d7a03a 50%,#8a4a1e 80%)}
.photo-pizza{left:708px;top:488px;width:172px;height:88px;background:radial-gradient(ellipse,#d9402a,#c8291c 55%,#e8b060 78%)}
.photo-cans{left:556px;top:745px;width:66px;height:86px;border-radius:8px;background:linear-gradient(90deg,#e8d87a,#a8c848)}
.photo-pints{left:760px;top:762px;width:86px;height:80px;border-radius:6px;background:linear-gradient(180deg,#c9b9a8 0%,#2a1410 25%,#1a0c08 100%)}

.day{text-align:center}
.day-name{font-family:"Arvo",serif;font-weight:700;font-size:25px;letter-spacing:1px;border-bottom:2px solid var(--white);padding-bottom:2px;display:inline-block}
.day-feature{font-family:"Arvo",serif;font-weight:700;font-size:17px;line-height:19px;margin-top:10px;text-transform:uppercase}
.specials{list-style:none;text-align:left;font-size:14px;line-height:17.5px}
.specials li{display:flex}
.specials .price{width:30px;flex:none}
.specials-lg{font-size:17px;line-height:25px}
.specials-lg .price{width:28px}
.note{font-size:17px;line-height:24px;text-align:center}
.sub-label{font-size:14px;text-transform:uppercase;margin:14px 0 4px}

.coupon{top:1097px;height:103px}
.coupon-pizza{left:0;width:242px;background:var(--green)}
.coupon-philly{left:242px;width:245px;background:var(--orange)}
.contact{left:487px;width:447px;background:var(--red)}
.coupon-amount{font-family:"Roboto",sans-serif;font-weight:900;font-size:34px;line-height:34px}
.coupon-item{font-family:"Roboto",sans-serif;font-weight:900}
.slice{left:160px;top:40px;width:72px;height:48px;border-radius:6px;background:linear-gradient(135deg,#e9b25c,#d2402a)}
.contact-line{font-family:"Roboto Condensed",sans-serif;font-weight:700}
</style>
</head>
<body>

<div class="abs hero-photo" role="img" aria-label="Two frosted mugs of draft beer on a dark background"></div>
<div class="abs wood" role="img" aria-label="Warm brown wood plank backdrop"></div>
<svg class="abs hero-curve" width="934" height="60" viewBox="0 0 934 60">
  <path d="M0 38 Q 420 8 934 14" fill="none" stroke="var(--orange)" stroke-width="6"/>
</svg>

<div class="abs brand"><span class="brand-dot"></span><span class="brand-name">LARKFOLD INN</span></div>

<h1 class="abs title">Happy Hours</h1>
<p class="abs hours">Domestic Drafts Every Day<br>Mon-Fri 3-7 • Sat &amp; Sun 12-7</p>
<div class="abs big-price"><span>$1</span></div>

<!-- food and drink photos -->
<div class="abs photo-mug" role="img" aria-label="Mug of beer beside a billiard eight ball"></div>
<div class="abs photo photo-philly" role="img" aria-label="Philly cheese steak sandwich with fries"></div>
<div class="abs photo photo-nachos" role="img" aria-label="Plate of loaded nachos"></div>
<div class="abs photo photo-pizza" role="img" aria-label="Pepperoni pizza"></div>
<div class="abs photo-cans" role="img" aria-label="Two cans of pineapple beer"></div>
<div class="abs photo-pints" role="img" aria-label="Three pints of dark beer"></div>

<!-- price badges -->
<div class="abs price-badge" style="left:92px;top:503px">$1</div>
<div class="abs price-badge" style="left:242px;top:505px">$6</div>
<div class="abs price-badge" style="left:462px;top:505px">$3</div>
<div class="abs price-badge" style="left:686px;top:505px">$4</div>
<div class="abs price-badge" style="left:475px;top:768px">$2</div>
<div class="abs price-badge" style="left:685px;top:768px">$2</div>

<!-- Sundays -->
<section class="abs day" style="left:50px;top:763px;width:190px">
  <h2 class="day-name">SUNDAYS</h2>
  <p class="day-feature" style="font-size:19px;line-height:23px">Free Pool<br>All Day on<br>Both Tables</p>
  <p class="note" style="margin-top:22px;font-size:16px">$1.00 Domestic drafts<br>until midnight</p>
  <ul class="specials specials-lg" style="margin:22px 0 0 24px">
    <li><span class="price">$3</span>Appetizers</li>
    <li><span class="price">$4</span>Glacine<br>Bloody Marys</li>
    <li><span class="price">$5</span>3-Topping Pizza</li>
  </ul>
</section>

<!-- Mondays -->
<section class="abs day" style="left:270px;top:581px;width:190px">
  <h2 class="day-name">MONDAYS</h2>
  <p class="day-feature">Philly Cheese<br>Steak Sandwich<br>Served With<br>Loaded Fries</p>
  <ul class="specials" style="margin:12px 0 0 6px">
    <li><span class="price">$2</span>Well Margaritas</li>
    <li><span class="price">$3</span>5 Pebble Vodka Bombs</li>
    <li><span class="price">$4</span>Rum Runners</li>
  </ul>
</section>

<!-- Thursdays -->
<section class="abs day" style="left:263px;top:781px;width:182px">
  <h2 class="day-name">THURSDAYS</h2>
  <p class="day-feature">*Ladies Night<br>Thursday*</p>
  <ul class="specials" style="margin:16px 0 0 12px;line-height:21px">
    <li><span class="price">$3</span>Tart Crumb</li>
    <li><span class="price">$3</span>Sweet Affair</li>
    <li><span class="price">$3</span>1/2 dozen wings!</li>
    <li><span class="price">$4</span>Spin Doctors</li>
  </ul>
  <p class="sub-label" style="text-align:left;margin-left:12px;margin-top:18px">Ladies Only Specials</p>
  <ul class="specials" style="margin-left:12px;line-height:21px">
    <li><span class="price">$2</span>5 Pebble Shots</li>
    <li><span class="price">$3</span>Long Islands</li>
    <li><span class="price">$4</span>Bartender Bombs!</li>
  </ul>
</section>

<!-- Tuesdays -->
<section class="abs day" style="left:480px;top:581px;width:180px">
  <h2 class="day-name">TUESDAYS</h2>
  <p class="day-feature">Loaded<br>Nachos &amp; Fries</p>
  <ul class="specials" style="margin:14px 0 0 12px">
    <li><span class="price">$2</span>Harvest Radler</li>
    <li><span class="price">$3</span>Gray Heron</li>
    <li><span class="price">$4</span>Liquid Marijuana's</li>
  </ul>
</section>

<!-- Wednesdays -->
<section class="abs day" style="left:692px;top:581px;width:200px">
  <h2 class="day-name">WEDNESDAYS</h2>
  <p class="day-feature">2 Toppings<br>Pizzas</p>
  <ul class="specials" style="margin:14px 0 0 18px">
    <li><span class="price">$2</span>Quiet Meadow Bottles</li>
    <li><span class="price">$3</span>Blue Stars</li>
    <li><span class="price">$3</span>Fizzle Twigs</li>
    <li><span class="price">$4</span>Bartender Bombs</li>
  </ul>
</section>

<!-- Fridays -->
<section class="abs day" style="left:470px;top:845px;width:195px">
  <h2 class="day-name">FRIDAYS</h2>
  <p class="day-feature">Mele Nalu<br>Pineapple Beer</p>
  <ul class="specials" style="margin:16px 0 0 12px">
    <li><span class="price">$2</span>Lumbermans Brew</li>
    <li><span class="price">$2</span>Knotted Cup</li>
    <li><span class="price">$2</span>Restless Rover</li>
    <li><span class="price">$3</span>Little Beers</li>
    <li><span class="price">$3</span>Banana Pepper Rings</li>
    <li><span class="price">$3</span>Hot Pepper Cheese Balls</li>
    <li><span class="price">$4</span>Washington Apples</li>
  </ul>
</section>

<!-- Saturdays -->
<section class="abs day" style="left:688px;top:848px;width:196px">
  <h2 class="day-name">SATURDAYS</h2>
  <p class="day-feature">Extended Happy<br>Hour (12–8PM)</p>
  <ul class="specials" style="margin:16px 0 0 16px">
    <li><span class="price">$1</span>Domestic Drafts</li>
    <li><span class="price">$2</span>Wine Coolers</li>
    <li><span class="price">$2</span>Lumbermans Brew</li>
    <li><span class="price">$2</span>Pellows Hard Iced Tea</li>
    <li><span class="price">$3</span>Sweet Affair</li>
    <li><span class="price">$3</span>Irish Breakfast Shots</li>
    <li><span class="price">$4</span>Irish Car Bombs</li>
    <li><span class="price">$4</span>Orbit Lollies</li>
  </ul>
</section>

<!-- coupons and contact -->
<div class="abs coupon coupon-pizza">
  <p class="abs coupon-amount" style="left:20px;top:14px">$2.00 OFF</p>
  <p class="abs coupon-item" style="left:22px;top:48px;font-size:46px;line-height:46px">PIZZA</p>
  <div class="abs slice" role="img" aria-label="Slice of pepperoni pizza"></div>
</div>
<div class="abs coupon coupon-philly">
  <p class="abs coupon-amount" style="left:20px;top:14px">$2.00 OFF</p>
  <p class="abs coupon-item" style="left:22px;top:50px;font-size:21px;line-height:21px">PHILLY CHEESE<br>STEAK</p>
</div>
<div class="abs coupon contact">
  <p class="abs contact-line" style="left:10px;top:16px;font-size:19px">T (440) 555-0193</p>
  <p class="abs contact-line" style="left:178px;top:18px;font-size:16px;font-weight:400">Join Us on Gathergram\Larkfoldinn</p>
  <p class="abs contact-line" style="left:91px;top:48px;font-size:16px;font-weight:400">418 West Cedar Avenue Wellington, Ohio 44987</p>
  <p class="abs contact-line" style="left:52px;top:72px;font-size:12.5px">Contact for us for birthday party discounts and fund raising events</p>
</div>

</body>
</html>
```